Notepads for Marketing pieces-BOLD design

Looking for notepads for marketing pieces with logo, phone number, and website. Maybe something faded in background. Looking for bold and different

```html
<!DOCTYPE html>
<html lang="en">
<head>
<meta charset="utf-8">
<title>Vantacare Letterhead</title>
<link rel="stylesheet" href="https://fonts.googleapis.com/css2?family=Poppins:wght@400;500;600;700&display=swap">
<style>
  :root {
    --brand-red: #ff0000;
    --ink: #111111;
    --paper: #ffffff;
  }
  * { margin: 0; padding: 0; box-sizing: border-box; }
  html, body { width: 848px; height: 1200px; overflow: hidden; background: var(--paper); }
  .sheet {
    position: relative;
    width: 848px;
    height: 1200px;
    background: var(--paper);
    font-family: "Poppins", sans-serif;
    color: var(--ink);
  }
  .header-band { position: absolute; top: 0; left: 0; width: 848px; height: 160px; }
  .brand-name {
    position: absolute;
    left: 53px;
    top: 44px;
    font-size: 44px;
    font-weight: 700;
    letter-spacing: 1px;
    color: var(--brand-red);
    line-height: 1;
  }
  .brand-tagline {
    position: absolute;
    left: 36px;
    top: 116px;
    font-size: 11px;
    font-weight: 500;
    color: var(--ink);
  }
  .contact-block {
    position: absolute;
    right: 36px;
    top: 28px;
    text-align: right;
    color: var(--paper);
    font-size: 15px;
    line-height: 25.5px;
  }
  .contact-block .company { font-weight: 600; }
  .social-row {
    position: absolute;
    top: 1109px;
    left: 36px;
    right: 36px;
    height: 20px;
    display: flex;
    justify-content: space-between;
    align-items: center;
  }
  .social-item {
    display: flex;
    align-items: center;
    gap: 16px;
    color: var(--brand-red);
    font-size: 15px;
    font-weight: 500;
  }
  .social-marker {
    width: 17px;
    height: 17px;
    border-radius: 3px;
    background: var(--brand-red);
  }
  .footer-band {
    position: absolute;
    left: 0;
    bottom: 0;
    width: 848px;
    height: 46px;
    background: var(--brand-red);
    display: flex;
    align-items: center;
    justify-content: center;
    color: var(--paper);
    font-size: 14px;
    font-weight: 600;
    letter-spacing: 2px;
  }
</style>
</head>
<body>
  <div class="sheet">
    <svg class="header-band" width="848" height="160" viewBox="0 0 848 160" aria-hidden="true">
      <polygon points="513,0 848,0 848,157 460,157" fill="var(--brand-red)"/>
      <line x1="0" y1="158" x2="848" y2="158" stroke="var(--brand-red)" stroke-width="2.5"/>
    </svg>

    <div class="brand-name">VANTACARE</div>
    <div class="brand-tagline">Home Health | Medical Staffing | Outpatient Therapy</div>

    <div class="contact-block">
      <div class="company">Vantacare Therapy Partners</div>
      <div>admin@vantacare.org</div>
      <div>555.214.0180 555.214.0193</div>
      <div>4870 Meridian Way Ashford, OH 43990</div>
    </div>

    <div class="social-row">
      <div class="social-item"><span class="social-marker"></span>vantacare</div>
      <div class="social-item"><span class="social-marker"></span>@vantacarellc</div>
      <div class="social-item"><span class="social-marker"></span>vantacare</div>
    </div>

    <div class="footer-band">https://vantacare.org</div>
  </div>
</body>
</html>
```